Tallowind Concrete

We are looking for a design for a two sided over-sized postcard to show the beauty of the work we provide. We want it to be simple, bold & elegant as well as eye catching. Feel free to crop the images supplied to whatever looks best.

Website is www.twq-plains.com for more information, verbiage, contact information, etc.

```html
<!DOCTYPE html>
<html lang="en">
<head>
<meta charset="utf-8">
<title>Tallowind Concrete — Postcard</title>
<link rel="stylesheet" href="https://fonts.googleapis.com/css2?family=Roboto+Condensed:wght@700&family=Arimo:wght@400;700&display=swap">
<style>
  :root {
    --backdrop: #6f6b6a;
    --paper: #ffffff;
    --brown: #4f3e36;
    --green: #8dc63f;
    --arrow: #f3e500;
    --white: #ffffff;
  }
  html, body {
    margin: 0;
    width: 1200px;
    height: 864px;
    overflow: hidden;
    background: var(--backdrop);
  }
  .postcard { display: block; width: 1200px; height: 864px; }
  .card-face { fill: var(--paper); }
  .site-url { font-family: "Arimo", Arial, sans-serif; font-size: 22px; fill: var(--brown); }
  .headline { font-family: "Roboto Condensed", "Arial Narrow", sans-serif; font-weight: 700; font-size: 49px; fill: var(--brown); }
  .brand-name { font-family: "Roboto Condensed", "Arial Narrow", sans-serif; font-weight: 700; font-size: 42px; fill: var(--brown); }
  .brand-mark { fill: var(--green); }
  .call-now { font-family: "Arimo", Arial, sans-serif; font-weight: 700; font-size: 30px; fill: var(--green); }
  .phone { font-family: "Arimo", Arial, sans-serif; font-size: 36px; fill: var(--brown); }
  .service-band { fill: var(--green); }
  .service { font-family: "Roboto Condensed", "Arial Narrow", sans-serif; font-weight: 700; font-size: 24px; fill: var(--white); }
  .service-arrow { fill: var(--arrow); }
</style>
</head>
<body>
<svg class="postcard" viewBox="0 0 1200 864" xmlns="http://www.w3.org/2000/svg">
  <defs>
    <linearGradient id="patio-tones" x1="0" y1="0" x2="1" y2="1">
      <stop offset="0" stop-color="#6f8f4a"/>
      <stop offset="0.35" stop-color="#8f8a80"/>
      <stop offset="0.7" stop-color="#9a8b78"/>
      <stop offset="1" stop-color="#5a4a40"/>
    </linearGradient>
    <linearGradient id="fence-tones" x1="0" y1="0" x2="0" y2="1">
      <stop offset="0" stop-color="#7f9a55"/>
      <stop offset="0.5" stop-color="#a0603a"/>
      <stop offset="1" stop-color="#5f7a3c"/>
    </linearGradient>
    <linearGradient id="slab-tones" x1="0" y1="0" x2="1" y2="1">
      <stop offset="0" stop-color="#7c8d5a"/>
      <stop offset="0.5" stop-color="#9c6e52"/>
      <stop offset="1" stop-color="#8aa060"/>
    </linearGradient>
  </defs>

  <rect class="card-face" x="84" y="100" width="1032" height="664"/>

  <text class="site-url" x="102" y="134">www.twq-plains.com</text>

  <polygon role="img" aria-label="Photo of a wet multicolour flagstone patio bordered by lawn, potted flowers and a red maple" fill="url(#patio-tones)" points="84,148 645,148 575,495 84,495"/>

  <g class="headline-block">
    <text class="headline" x="688" y="195">ENRICH &amp;</text>
    <text class="headline" x="678" y="254">PRESERVE YOUR</text>
    <text class="headline" x="664" y="312">STONE, CONCRETE</text>
    <text class="headline" x="648" y="371">OR WOOD!</text>
  </g>

  <polygon role="img" aria-label="Photo of a stained cedar fence behind a flowering garden and trees" fill="url(#fence-tones)" points="602,392 885,392 826,657 548,657"/>
  <polygon role="img" aria-label="Photo of a stamped, stained concrete patio beside a lawn" fill="url(#slab-tones)" points="906,392 1116,392 1116,562 860,562"/>

  <g class="brand">
    <rect class="brand-mark" x="128" y="538" width="86" height="86"/>
    <text class="brand-name" x="230" y="576">TALLOWIND</text>
    <text class="brand-name" x="230" y="622">CONCRETE</text>
  </g>

  <text class="call-now" x="966" y="611" text-anchor="middle">CALL NOW!</text>
  <text class="phone" x="967" y="649" text-anchor="middle">832-555-0147</text>

  <polygon class="service-band" points="84,674 1056,674 1028,764 84,764"/>
  <g class="services">
    <polygon class="service-arrow" points="108,692 116,700 108,708"/>
    <text class="service" x="127" y="709">ACID STAINING</text>
    <polygon class="service-arrow" points="322,692 330,700 322,708"/>
    <text class="service" x="338" y="709">SEALING &amp; WEATHERPROOFING</text>
    <polygon class="service-arrow" points="108,728 116,736 108,744"/>
    <text class="service" x="127" y="745">DECK &amp; FENCE STAINING &amp; SEALING</text>
    <polygon class="service-arrow" points="534,728 542,736 534,744"/>
    <text class="service" x="550" y="745">ACID STAINING</text>
    <polygon class="service-arrow" points="738,728 746,736 738,744"/>
    <text class="service" x="754" y="745">GARAGE EPOXY</text>
  </g>
</svg>
</body>
</html>
```